Gaming "Ember Tonic" Energy Drink CAN Design

Energy Drink called "Ember Tonic" which should include the classic Health Potions out of a video game like, Morvath, Realm of Ironvale, Crystal Odyssey, Stone Banners, Towers and Tempests and so on. Our Products is focused on gamers, geeks and nerds. DESIGN INFORMATION We want to have a design that fits the style of health potions we are looking for of a video game. The main color should be RED, which is the usual color for a Ember Tonic in a video game. The word "Ember Tonic" has become to be visible on the product foremost.
Updates

Langsam um Feedback zu geben

Target Market(s)

Gamers geeks and nerds

Font styles to use
Serif
Sans Serif
Decorative
Script

Colors
ec1f27

Requirements
Must have
• The Color Red has to be dominant, as the Ember Tonic is in a Video Game is Red
Nice to have
• Something that resembles a Ember Tonic out of a game like: Morvath, Realm of Ironvale, Crystal Odyssey

```html
<!DOCTYPE html>
<html lang="de">
<head>
<meta charset="utf-8">
<title>Ember Tonic – Energy Drink Dosenetikett</title>
<link href="https://fonts.googleapis.com/css2?family=Arimo:wght@400;700&display=swap" rel="stylesheet">
<style>
  :root {
    --stage: #1c0607;
    --can-red: #ec1f27;
    --can-red-deep: #d81a22;
    --ink-gold: #f6b15e;
    --ink-cream: #f7e3b8;
    --panel-peach: #e6a266;
    --brand-gold: #e9b64c;
  }
  * { margin: 0; padding: 0; box-sizing: border-box; }
  html, body { width: 778px; height: 1200px; overflow: hidden; }
  body {
    background: var(--stage);
    font-family: "Arimo", Arial, sans-serif;
    position: relative;
  }
  .label {
    position: absolute;
    left: 19px; top: 320px;
    width: 740px; height: 561px;
    background: radial-gradient(ellipse at 60% 45%, var(--can-red) 0%, var(--can-red-deep) 100%);
    color: var(--ink-gold);
    font-size: 7.6px;
    line-height: 10.4px;
    box-shadow: 0 6px 24px rgba(0,0,0,.45);
  }
  .info-block { position: absolute; left: 34px; }
  .ingredients { top: 47px; width: 200px; }
  .ingredients strong { font-weight: 700; }
  .nutrition {
    position: absolute; left: 34px; top: 163px;
    width: 199px; height: 182px;
    border: 1.5px solid var(--ink-gold);
    padding: 3px 4px;
  }
  .nutrition table { width: 100%; border-collapse: collapse; table-layout: fixed; }
  .nutrition td { padding: 0; vertical-align: top; white-space: nowrap; overflow: hidden; }
  .nutrition .num { text-align: right; }
  .nutrition .sub { padding-left: 10px; }
  .nutrition .head td { font-weight: 700; }
  .facts .name { width: 68%; }
  .vitamins { margin-top: 10px; }
  .vitamins .name { width: 46%; }
  .vitamins .amount { width: 27%; }
  .footnotes { margin-top: 10px; }
  .handling { top: 352px; width: 126px; }
  .handling p + p { margin-top: 8px; }
  .batch-panel {
    position: absolute; left: 165px; top: 352px;
    width: 68px; height: 158px;
    background: var(--panel-peach);
  }
  .volume-mark {
    position: absolute; left: 167px; top: 512px;
    font-size: 15px; line-height: 18px; font-weight: 700;
    color: var(--ink-cream);
  }
  .volume-mark .estimated { font-size: 20px; font-weight: 400; }
  .brand {
    position: absolute; left: 329px; top: 186px; width: 300px;
    text-align: center;
  }
  .brand-name {
    font-size: 32px; line-height: 38px; font-weight: 700;
    color: var(--brand-gold);
  }
  .brand-tag {
    margin-top: 6px;
    font-size: 10px; line-height: 12px; letter-spacing: .5px;
    color: var(--ink-gold);
  }
  .front-volume {
    position: absolute; left: 428px; top: 486px; width: 100px;
    text-align: center;
    font-size: 13px; line-height: 16px; color: var(--ink-cream);
  }
</style>
</head>
<body>
  <section class="label">
    <div class="info-block ingredients">
      <strong>ENERGY DRINK – PFANDFREI<br>ERHÖHTER KOFFEINGEHALT (32mg/100ml)<br>ZUTATEN:</strong>
      MOLKENERZEUGNIS*, WASSER, ZUCKER, SÄUERUNGSMITTEL E330, KOHLENSÄURE, SÄUREREGULATOREN: E331, E332; KARAMELLISIERTER ZUCKER, AROMA, GLUKURONOLAKTON (0,04%), TAURIN (0,04%), KOFFEIN (0,03%), INOSIT (0,02%), VITAMINE: NIACIN, PANTOTHENSÄURE, VITAMIN B6, VITAMIN B12; FARBSTOFFE: E150d, E101
    </div>

    <div class="nutrition">
      <table class="facts">
        <tr class="head"><td class="name">NÄHRWERTE</td><td class="num">IN 100ml</td></tr>
        <tr><td class="name">BRENNWERT</td><td class="num">198 kJ / 47 kcal</td></tr>
        <tr><td class="name">FETT</td><td class="num">0 g</td></tr>
        <tr><td class="name sub">DAVON GESÄTTIGTE FETTSÄUREN</td><td class="num">0 g</td></tr>
        <tr><td class="name">KOHLENHYDRATE</td><td class="num">11,1 g</td></tr>
        <tr><td class="name sub">DAVON ZUCKER</td><td class="num">10,9 g</td></tr>
        <tr><td class="name">EIWEISS</td><td class="num">0 g</td></tr>
        <tr><td class="name">SALZ</td><td class="num">&lt; 0,1 g</td></tr>
      </table>
      <table class="vitamins">
        <tr class="head"><td class="name">VITAMINE</td><td class="amount num">IN 100ml</td><td class="num">% NRV**</td></tr>
        <tr><td class="name">NIACIN</td><td class="amount num">7,04 mg</td><td class="num">44%</td></tr>
        <tr><td class="name">VITAMIN B6</td><td class="amount num">1,4 mg</td><td class="num">100%</td></tr>
        <tr><td class="name">VITAMIN B12</td><td class="amount num">5,0 µg</td><td class="num">200%</td></tr>
        <tr><td class="name">PANTOTHENSÄURE</td><td class="amount num">1,98 mg</td><td class="num">33%</td></tr>
      </table>
      <p class="footnotes">* ENTHÄLT EIN MILCHERZEUGNIS<br>**% DER NÄHRSTOFFBEZUGSWERTE</p>
    </div>

    <div class="info-block handling">
      <p>GEKÜHLT TRINKEN<br>PASTEURISIERT</p>
      <p>IN MODERATEN MENGEN KONSUMIEREN.<br>FÜR KINDER UND SCHWANGERE ODER STILLENDE FRAUEN NICHT EMPFOHLEN.</p>
      <p>HERGESTELLT IN ÖSTERREICH VON KESSELWERK ABFÜLLUNG &amp; ENTWICKLUNG GMBH<br>FÜR XXXXXXXXXXXXXXX<br>XXXXXXXXXXXXXXXXX<br>XXXXXXXX</p>
      <p>MINDESTENS HALTBAR BIS:<br>SIEHE DOSENBODEN</p>
    </div>
    <div class="batch-panel" aria-label="Feld für Chargen- und Datumsaufdruck"></div>
    <div class="volume-mark"><span class="estimated">℮</span>250ml</div>

    <div class="brand">
      <div class="brand-name">Ember Tonic</div>
      <div class="brand-tag">ENERGY DRINK</div>
    </div>
    <div class="front-volume">250 ml</div>
  </section>
</body>
</html>
```